Real Estate Company Needs Business Card Designed

We need a business card design for a new real estate company based in Campbell, CA (Silicon Valley). We plan to improve the residential real estate industry by using technology to improve customer experience. We would like to see designs that use a black background. The final design should communicate sophistication and customer service, as well as stability and technology.

Industry/Entity Type

Real Estate

Requirements
Must have
• Black background

```html
<!DOCTYPE html>
<html lang="en">
<head>
<meta charset="utf-8">
<title>Norvell – Business Card</title>
<link rel="stylesheet" href="https://fonts.googleapis.com/css2?family=Arimo:wght@400;700&display=swap">
<style>
  :root {
    --backdrop: #e4e1df;
    --card-black: #0d0d0e;
    --band-dark: #1b1c1e;
    --band-light: #2a2b2e;
    --divider-light: #3a3b3e;
    --text-light: #d9d9db;
    --text-soft: #bfc0c3;
    --logo-tone: #c7cfdc;
    --icon-fill: #d4d4d6;
    --icon-glyph: #1a1a1c;
  }
  * { margin: 0; padding: 0; box-sizing: border-box; }
  html, body {
    width: 1200px;
    height: 1000px;
    overflow: hidden;
    background: var(--backdrop);
    font-family: "Arimo", Arial, sans-serif;
  }
  .business-card {
    position: absolute;
    left: 100px;
    top: 215px;
    width: 1000px;
    height: 570px;
    background: var(--card-black);
    overflow: hidden;
  }
  .card-art {
    position: absolute;
    inset: 0;
    width: 1000px;
    height: 570px;
  }
  .brand-name {
    position: absolute;
    left: 80px;
    top: 258px;
    font-size: 70px;
    font-weight: 400;
    letter-spacing: 2px;
    color: var(--logo-tone);
    line-height: 1;
  }
  .holder {
    position: absolute;
    left: 500px;
    top: 52px;
    color: var(--text-light);
  }
  .holder-name {
    font-size: 40px;
    font-weight: 400;
    line-height: 1.05;
  }
  .holder-role {
    font-size: 24px;
    color: var(--text-soft);
    margin-left: 34px;
    margin-top: 4px;
  }
  .contact-list {
    position: absolute;
    left: 590px;
    top: 200px;
    list-style: none;
  }
  .contact-item {
    display: flex;
    align-items: center;
    height: 34px;
    margin-bottom: 18px;
    font-size: 21px;
    color: var(--text-light);
    white-space: nowrap;
  }
  .contact-icon {
    width: 32px;
    height: 32px;
    margin-right: 14px;
    flex: none;
  }
</style>
</head>
<body>
  <main class="business-card">
    <svg class="card-art" viewBox="0 0 1000 570" aria-hidden="true">
      <defs>
        <linearGradient id="bandTone" x1="0" y1="0" x2="1" y2="1">
          <stop offset="0" stop-color="var(--band-light)"/>
          <stop offset="1" stop-color="var(--band-dark)"/>
        </linearGradient>
        <linearGradient id="dividerShade" x1="0" y1="0" x2="1" y2="0">
          <stop offset="0" stop-color="#000" stop-opacity="0.7"/>
          <stop offset="1" stop-color="#000" stop-opacity="0"/>
        </linearGradient>
      </defs>
      <polygon class="feature-band" points="0,190 500,190 577,400 0,400" fill="url(#bandTone)"/>
      <polygon class="divider-shade" points="430,0 460,0 670,570 640,570" fill="url(#dividerShade)"/>
      <line class="divider-line" x1="430" y1="0" x2="640" y2="570" stroke="var(--divider-light)" stroke-width="1.5"/>
    </svg>

    <div class="brand-name">NORVELL</div>

    <section class="holder">
      <h1 class="holder-name">Daniel Reyes</h1>
      <p class="holder-role">general manager</p>
    </section>

    <ul class="contact-list">
      <li class="contact-item">
        <svg class="contact-icon" viewBox="0 0 32 32" aria-hidden="true">
          <rect width="32" height="32" rx="5" fill="var(--icon-fill)"/>
          <path d="M16 7 L26 16 H23 V25 H18.5 V19.5 H13.5 V25 H9 V16 H6 Z" fill="var(--icon-glyph)"/>
        </svg>
        45 Orchard Lane, Alder Park
      </li>
      <li class="contact-item">
        <svg class="contact-icon" viewBox="0 0 32 32" aria-hidden="true">
          <rect width="32" height="32" rx="5" fill="var(--icon-fill)"/>
          <path d="M10 7 L13.5 7 L15 12 L12.8 13.6 C13.8 16 15.8 18.2 18.4 19.2 L20 17 L25 18.5 L25 22 C25 23.5 23.8 25 22 25 C14 24.5 7.5 18 7 10 C7 8.2 8.5 7 10 7 Z" fill="var(--icon-glyph)"/>
        </svg>
        + 408 555 0142
      </li>
      <li class="contact-item">
        <svg class="contact-icon" viewBox="0 0 32 32" aria-hidden="true">
          <rect width="32" height="32" rx="5" fill="var(--icon-fill)"/>
          <text x="16" y="22.5" text-anchor="middle" font-family="Arimo, Arial, sans-serif" font-size="19" fill="var(--icon-glyph)">@</text>
        </svg>
        hello@norvellhomes.com
      </li>
      <li class="contact-item">
        <svg class="contact-icon" viewBox="0 0 32 32" aria-hidden="true">
          <rect width="32" height="32" rx="5" fill="var(--icon-fill)"/>
          <circle cx="16" cy="16" r="8.5" fill="none" stroke="var(--icon-glyph)" stroke-width="2"/>
        </svg>
        www.norvellhomes.com
      </li>
    </ul>
  </main>
</body>
</html>
```